Brivane - Business Cards for a new venture

create business card for a startup classified business dealing in construction materials, the cards need to have a professional look but modern, more serious than playful, one of the samples must include the official font (attached), please explore using the official colors in the company's logo

Target Market(s)

Energy sector

Contact Information for Business Card

Font styles to use
Other font styles liked:
• suissnord

Requirements
Must have
• corporate colors (in logo attached)
Nice to have
• Official font (in one of the samples) font is : suissnord
Should not have
• Cartoonish look

```html
<!DOCTYPE html>
<html lang="en">
<head>
<meta charset="utf-8">
<title>Brivane – Business Cards</title>
<link rel="stylesheet" href="https://fonts.googleapis.com/css2?family=Orbitron:wght@400;500&display=swap">
<style>
  :root {
    --canvas: #ffffff;
    --card-white: #ffffff;
    --card-grey: #949499;
    --brand-grey: #939598;
    --brand-navy: #043e6f;
    --ink-white: #ffffff;
    --frame: #111111;
  }
  * { box-sizing: border-box; margin: 0; padding: 0; }
  html, body {
    width: 1200px; height: 1000px; overflow: hidden;
    background: var(--canvas);
    font-family: "Orbitron", sans-serif;
  }
  .canvas { position: relative; width: 1200px; height: 1000px; }

  .card {
    position: absolute; left: 310px; width: 580px; height: 351px;
    border: 2px solid var(--frame);
    overflow: hidden;
  }
  .card--front { top: 125px; background: var(--card-white); }
  .card--back  { top: 523px; background: var(--card-grey); }

  /* front */
  .front-mark {
    position: absolute; left: 50%; top: 92px; width: 70px; height: 70px;
    margin-left: -35px; border-radius: 50%; background: var(--brand-navy);
  }
  .front-name {
    position: absolute; left: 0; right: 0; top: 238px;
    text-align: center; font-size: 33px; font-weight: 400;
    letter-spacing: 4px; color: var(--brand-grey); text-transform: uppercase;
  }

  /* back */
  .back-mark {
    position: absolute; left: 112px; top: 128px; width: 32px; height: 32px;
    border-radius: 50%; background: var(--ink-white);
  }
  .back-name {
    position: absolute; left: 38px; width: 180px; top: 205px;
    text-align: center; font-size: 17px; letter-spacing: 2px;
    color: var(--ink-white); text-transform: uppercase;
  }
  .divider {
    position: absolute; left: 238px; top: 30px; width: 2px; height: 237px;
    background: var(--ink-white);
  }
  .holder {
    position: absolute; right: 17px; top: 33px; text-align: right;
    color: var(--ink-white); text-transform: uppercase;
    font-size: 16px; letter-spacing: 1.5px; line-height: 26px;
  }
  .contacts { list-style: none; }
  .contact {
    position: absolute; left: 260px; right: 15px; height: 22px;
    color: var(--ink-white); text-transform: uppercase;
    font-size: 12px; letter-spacing: 1px;
    display: flex; align-items: center; justify-content: space-between;
  }
  .contact svg { width: 22px; height: 22px; fill: none; stroke: var(--ink-white); stroke-width: 1.3; }
  .contact--mobile { top: 127px; }
  .contact--office { top: 172px; }
  .contact--email  { top: 204px; }
  .contact--web    { top: 237px; }

  .address-band {
    position: absolute; left: 0; right: 0; bottom: 0; height: 53px;
    background: var(--brand-navy); color: var(--ink-white);
    display: flex; align-items: center; justify-content: center;
    font-size: 14px; letter-spacing: 1.5px; text-transform: uppercase;
  }
</style>
</head>
<body>
<main class="canvas">
  <section class="card card--front">
    <span class="front-mark" aria-hidden="true"></span>
    <p class="front-name">Brivane</p>
  </section>

  <section class="card card--back">
    <span class="back-mark" aria-hidden="true"></span>
    <p class="back-name">Brivane</p>
    <span class="divider" aria-hidden="true"></span>

    <div class="holder">
      <p class="holder-name">Name</p>
      <p class="holder-role">Designation</p>
    </div>

    <ul class="contacts">
      <li class="contact contact--mobile">
        <svg viewBox="0 0 22 22" aria-hidden="true"><rect x="7" y="4" width="8" height="15" rx="1"/><line x1="9" y1="1" x2="9" y2="4"/><rect x="8.5" y="6" width="5" height="4"/></svg>
        <span>Cellular Number</span>
      </li>
      <li class="contact contact--office">
        <svg viewBox="0 0 22 22" aria-hidden="true" style="fill:var(--ink-white);stroke:none"><path d="M7 3c1 0 2 3 2 4s-1.5 1.5-1.5 2.5 2.5 5 3.5 5 1.3-1.3 2-1.3 3 1.5 3 2.5-1.5 2.3-3 2.3C9 18 5 11 5 6c0-1.5 1-3 2-3z"/></svg>
        <span>Office Number</span>
      </li>
      <li class="contact contact--email">
        <svg viewBox="0 0 22 22" aria-hidden="true" style="fill:var(--ink-white);stroke:var(--card-grey)"><rect x="2" y="4" width="18" height="13"/><polyline points="2,4 11,12 20,4"/></svg>
        <span>name@brivane.co.uk</span>
      </li>
      <li class="contact contact--web">
        <svg viewBox="0 0 22 22" aria-hidden="true"><circle cx="11" cy="11" r="9"/><ellipse cx="11" cy="11" rx="4" ry="9"/><line x1="2" y1="11" x2="20" y2="11"/><line x1="11" y1="2" x2="11" y2="20"/><path d="M4 6h14M4 16h14"/></svg>
        <span>www.brivane.co.uk</span>
      </li>
    </ul>

    <footer class="address-band">Physical Address</footer>
  </section>
</main>
</body>
</html>
```